Tall Harbor Business Card

We are a Video Production and Video Equipment Rental company specialising in the supply of state of the art Video Technology and Services for the Live Entertainment, Television and Corporate Business Theatre markets. (in Sydney, Australia) www.tallharbor-media.example

Industry/Entity Type

Business

Contact Information for Business Card

name, position, email, website, address, logo
Example attached of the information we need - doesn't necessarily have to look the same

Font styles to use
Other font styles liked:
• Tall Harbor logo font is GOTHAM

Colors
ea1f27

Requirements
Nice to have
• either matt black or shiny black cards -
raised logo

```html
<!DOCTYPE html>
<html lang="en">
<head>
<meta charset="utf-8">
<title>Tall Harbor Business Card</title>
<link href="https://fonts.googleapis.com/css2?family=Montserrat:wght@600&family=Open+Sans:wght@400;600;700&display=swap" rel="stylesheet">
<style>
  :root {
    --stage: #e9e9e9;
    --card-front: #ffffff;
    --card-back: #f4f3f1;
    --brand-red: #ea1f27;
    --ink: #1a1a1a;
    --ink-soft: #333333;
  }
  * { box-sizing: border-box; margin: 0; padding: 0; }
  html, body { width: 1200px; height: 675px; overflow: hidden; }
  body {
    background: var(--stage);
    font-family: "Open Sans", Arial, sans-serif;
    color: var(--ink);
    position: relative;
  }
  .card {
    position: absolute;
    top: 190px;
    width: 510px;
    height: 292px;
    box-shadow: 0 2px 6px rgba(0,0,0,0.12);
    overflow: hidden;
  }
  .card--front { left: 60px; background: var(--card-front); display: flex; align-items: center; justify-content: center; }
  .card--back { left: 630px; background: var(--card-back); }

  .wordmark {
    font-family: "Montserrat", Arial, sans-serif;
    font-weight: 600;
    color: var(--ink);
    text-transform: uppercase;
    letter-spacing: 0.02em;
    white-space: nowrap;
  }
  .wordmark--large { font-size: 44px; }
  .wordmark--small { font-size: 21px; }

  .back-logo { position: absolute; left: 34px; top: 98px; }

  .contact { position: absolute; left: 268px; top: 84px; }
  .contact__name {
    font-size: 15px; font-weight: 600; color: var(--brand-red);
    text-transform: uppercase; letter-spacing: 0.02em;
  }
  .contact__role { font-size: 10px; color: var(--ink-soft); margin-top: 1px; }
  .contact__list { list-style: none; margin-top: 12px; }
  .contact__item {
    display: flex; align-items: center; gap: 8px;
    font-size: 10.5px; color: var(--ink-soft); line-height: 1.75;
  }
  .contact__item svg { width: 11px; height: 11px; flex: none; fill: var(--brand-red); }

  .services-band {
    position: absolute; left: 0; right: 0; bottom: 0; height: 58px;
    background: var(--brand-red);
    display: flex; align-items: center; justify-content: flex-end;
    padding-right: 22px;
    font-size: 12.5px; font-weight: 700; color: var(--ink);
    white-space: nowrap;
  }
  .services-band .divider { margin: 0 6px; }
</style>
</head>
<body>
  <section class="card card--front" aria-label="Business card front">
    <span class="wordmark wordmark--large">Tall Harbor</span>
  </section>

  <section class="card card--back" aria-label="Business card back">
    <div class="back-logo"><span class="wordmark wordmark--small">Tall Harbor</span></div>

    <div class="contact">
      <p class="contact__name">Sam Ridley</p>
      <p class="contact__role">Managing Director</p>
      <ul class="contact__list">
        <li class="contact__item">
          <svg viewBox="0 0 12 12" aria-hidden="true"><path d="M6 0.5a4 4 0 0 0-4 4c0 3 4 7 4 7s4-4 4-7a4 4 0 0 0-4-4zm0 5.6a1.6 1.6 0 1 1 0-3.2 1.6 1.6 0 0 1 0 3.2z"/></svg>
          12 Wharf Road Marrick NSW 2000 Australia
        </li>
        <li class="contact__item">
          <svg viewBox="0 0 12 12" aria-hidden="true"><path d="M0.5 2.5h11v7h-11z" fill="none" stroke="#ea1f27" stroke-width="1.2"/><path d="M0.8 2.8L6 7l5.2-4.2" fill="none" stroke="#ea1f27" stroke-width="1.2"/></svg>
          sam@tallharbor-media.example
        </li>
        <li class="contact__item">
          <svg viewBox="0 0 12 12" aria-hidden="true"><circle cx="6" cy="6" r="5" fill="none" stroke="#ea1f27" stroke-width="1.1"/><path d="M1 6h10M6 1c-2.5 3-2.5 7 0 10M6 1c2.5 3 2.5 7 0 10" fill="none" stroke="#ea1f27" stroke-width="1"/></svg>
          www.tallharbor-media.example
        </li>
      </ul>
    </div>

    <div class="services-band">
      <span>Video Solution</span><span class="divider">|</span>
      <span>Led Screens</span><span class="divider">|</span>
      <span>Camera Systems</span><span class="divider">|</span>
      <span>Projection</span>
    </div>
  </section>
</body>
</html>
```